Business Card Design

Very plain simple card, Plain modern font. Background. Grey fading to black. Large Bright lime green text. Saying.

GLR-VU.COM

Small other details in white text.

Irish Horse Sales . Livery . Stud . Shows

Mark Dwyerson
GLR
Ashby Croft
Wolverdale Lane
Carbeckthorpe
Lincolnshire
LN7 2WT

Email. Glrvus@mailnest.co.uk
Tel. 07482 604319

Business

As below

```html
<!DOCTYPE html>
<html lang="en">
<head>
<meta charset="utf-8">
<title>GLR-VU.COM Business Card</title>
<link rel="stylesheet" href="https://fonts.googleapis.com/css2?family=Open+Sans:wght@400;800&display=swap">
<style>
  :root {
    --page-bg: #d9d9d9;
    --card-top: #7b7778;
    --card-mid: #2e2d2e;
    --card-bottom: #0d0d0d;
    --lime: #b5d334;
    --text-light: #ffffff;
  }
  html, body {
    margin: 0;
    padding: 0;
    width: 1200px;
    height: 1000px;
    overflow: hidden;
    background: var(--page-bg);
  }
  .canvas {
    width: 1200px;
    height: 1000px;
    display: flex;
    align-items: center;
    justify-content: center;
  }
  .business-card {
    width: 900px;
    height: 514px;
    box-sizing: border-box;
    background: linear-gradient(180deg, var(--card-top) 0%, var(--card-mid) 55%, var(--card-bottom) 100%);
    display: flex;
    flex-direction: column;
    align-items: center;
    font-family: "Open Sans", Arial, sans-serif;
    color: var(--text-light);
    padding-top: 120px;
  }
  .brand-name {
    margin: 0;
    font-weight: 800;
    font-size: 96px;
    line-height: 1;
    letter-spacing: 2px;
    color: var(--lime);
  }
  .services {
    margin: 14px 0 0;
    font-size: 22px;
    font-weight: 400;
    letter-spacing: 0.3px;
  }
  .contact {
    margin-top: 36px;
    font-style: normal;
    text-align: center;
    font-size: 18px;
    line-height: 1.4;
  }
  .contact-name {
    display: block;
    font-size: 16px;
  }
  .contact-line { display: block; }
</style>
</head>
<body>
  <main class="canvas">
    <section class="business-card" aria-label="Business card">
      <h1 class="brand-name">GLR-VU.COM</h1>
      <p class="services">Irish Horse Sales . Livery . Stud . Shows</p>
      <address class="contact">
        <span class="contact-name">Mark Dwyerson</span>
        <span class="contact-line">GLR, Ashby Croft, Wolverdale Lane</span>
        <span class="contact-line">Carbeckthorpe, Lincolnshire, LN7 2WT</span>
        <span class="contact-line">Email: Glrvus@mailnest.co.uk</span>
        <span class="contact-line">Tel: 07482 604319</span>
      </address>
    </section>
  </main>
</body>
</html>
```